Australian home builder requires inclusion list design

We require two inclusions list's flyers to showcase our two different inclusions. The design of the flyer is to reinforce professionalism and quality.
One inclusions list for each specification (i.e Orin and Cornerway)

Target Market(s)

Home Buyers aged 25 - 55

Industry/Entity Type

Home Builder

Other font styles liked:
• Harabara

```html
<!DOCTYPE html>
<html lang="en">
<head>
<meta charset="utf-8">
<title>Inclusions List</title>
<link href="https://fonts.googleapis.com/css2?family=Montserrat:wght@700;800&family=Poppins:wght@400;600&display=swap" rel="stylesheet">
<style>
  :root {
    --ink: #111111;
    --paper: #ffffff;
    --band-black: #0b0b0b;
    --panel-grey: #e4e4e4;
    --panel-green: #e2efdf;
    --accent-green: #b9dcb0;
    --text: #1a1a1a;
  }
  * { margin: 0; padding: 0; box-sizing: border-box; }
  html, body { width: 848px; height: 1200px; overflow: hidden; background: var(--paper); }
  .flyer { position: relative; width: 848px; height: 1200px; overflow: hidden; background: var(--paper);
    font-family: "Poppins", sans-serif; color: var(--text); }

  .photo { position: absolute; }
  .green-wash { position: absolute; left: 0; top: 0; width: 330px; height: 70px; background: var(--accent-green); opacity: .8; }
  .photo-painter { left: 20px; top: 0; width: 261px; height: 188px;
    background: linear-gradient(135deg, #6f8f7a 0%, #9fb5a4 45%, #c9d3c6 100%); }
  .photo-plans { left: 296px; top: 0; width: 258px; height: 186px;
    background: linear-gradient(160deg, #d9d6cf 0%, #b9b3a7 50%, #8c8a84 100%); }
  .photo-cables { left: 570px; top: 0; width: 259px; height: 188px;
    background: radial-gradient(circle at 60% 40%, #6a6a5c 0%, #2b2b26 40%, #070707 80%); }
  .photo-bath { left: 20px; top: 1043px; width: 261px; height: 157px;
    background: linear-gradient(180deg, #f1f1ef 0%, #cfd2d0 60%, #a9aba8 100%); }
  .photo-books { left: 296px; top: 1043px; width: 258px; height: 157px;
    background: linear-gradient(180deg, #3a3532 0%, #6c5d52 50%, #2a2624 100%); }
  .photo-roof { left: 570px; top: 1043px; width: 259px; height: 157px;
    background: linear-gradient(135deg, #c0603a 0%, #a44a2b 50%, #d27a52 100%); }
  .grey-veil { position: absolute; left: 112px; top: 1060px; width: 170px; height: 140px; background: #9a9a9a; opacity: .55; }
  .grey-veil-mid { position: absolute; left: 296px; top: 1043px; width: 110px; height: 157px; background: #9a9a9a; opacity: .45; }

  .section-title { position: absolute; height: 31px; background: var(--band-black); color: var(--paper);
    font-family: "Montserrat", sans-serif; font-weight: 800; font-size: 17px; letter-spacing: 2.4px;
    line-height: 31px; padding-left: 10px; text-transform: uppercase; }
  .panel { position: absolute; padding: 9px 10px; }
  .panel.grey { background: var(--panel-grey); }
  .panel.green { background: var(--panel-green); }

  .spec dt { font-size: 9.5px; font-weight: 600; text-transform: uppercase; letter-spacing: .4px; margin-top: 8px; }
  .spec dt:first-child { margin-top: 0; }
  .spec dd { font-size: 10.2px; line-height: 1.2; margin-top: 4px; letter-spacing: .2px; }
  .plain-list { list-style: none; font-size: 10.2px; line-height: 1.2; }
  .plain-list li { margin-bottom: 8.6px; }

  .contact { position: absolute; left: 570px; top: 886px; width: 259px; height: 143px; background: var(--band-black);
    color: var(--paper); padding: 12px 14px; font-size: 10.2px; line-height: 1.45; letter-spacing: .3px; }
  .contact p + p { margin-top: 16px; }
  .contact .line { margin-top: 4px; }
</style>
</head>
<body>
<div class="flyer">
  <div class="photo photo-painter" role="img" aria-label="Tradesperson finishing a plastered wall"></div>
  <div class="green-wash"></div>
  <div class="photo photo-plans" role="img" aria-label="House plans with a small model home"></div>
  <div class="photo photo-cables" role="img" aria-label="Close-up of electrical cable ends"></div>

  <!-- Left column -->
  <h2 class="section-title" style="left:20px;top:204px;width:261px;">Garage</h2>
  <div class="panel grey" style="left:20px;top:232px;width:261px;height:104px;">
    <dl class="spec">
      <dt>Garage Doors</dt><dd>Steelform panel lift door with two remotes from standard Colour Range</dd>
      <dt>External Access Doors</dt><dd>Solid Core External Door (Plan specific)</dd>
    </dl>
  </div>

  <h2 class="section-title" style="left:20px;top:353px;width:261px;">Internal Features</h2>
  <div class="panel green" style="left:20px;top:382px;width:261px;height:382px;">
    <dl class="spec">
      <dt>Ceiling Heights</dt><dd>2400mm</dd>
      <dt>Wall Linings</dt><dd>Plasterboard to wall linings and ceilings</dd><dd>Wetboard to Bathrooms and Ensuite</dd>
      <dt>Cornice</dt><dd>90mm Cove cornice</dd>
      <dt>Internal Doors</dt><dd>Hartwell Accent series 2040mm high door</dd>
      <dt>Door Furniture</dt><dd>Ashbury G4 Series</dd>
      <dt>Architraves</dt><dd>42mm x 12mm (selection available)</dd>
      <dt>Skirting</dt><dd>68 x 12mm (Selection Available)</dd>
      <dt>Windows Reveals</dt><dd>FJP Pine reveals to full perimeter of window</dd>
    </dl>
  </div>

  <h2 class="section-title" style="left:20px;top:776px;width:261px;">Paintwork</h2>
  <div class="panel green" style="left:20px;top:808px;width:261px;height:218px;">
    <dl class="spec">
      <dt>External</dt><dd>One colour to soffits and one colour to wall gloss acrylic plus one feature colour</dd>
      <dt>Internal Walls</dt><dd>Low sheen acrylic (3 coat system)</dd>
      <dt>Internal Ceilings</dt><dd>Ceiling Paint ( 3 coat system)</dd>
      <dt>Internal Woodwork and Doors</dt><dd>Semi-Gloss Finish to doors, architraves and skirtings</dd>
    </dl>
  </div>

  <!-- Middle column -->
  <h2 class="section-title" style="left:296px;top:204px;width:258px;">Insulation</h2>
  <div class="panel green" style="left:296px;top:235px;width:258px;height:57px;">
    <dl class="spec">
      <dt>Roof Insulation</dt><dd>60mm Thermacoat Roof Blanket</dd>
    </dl>
  </div>

  <h2 class="section-title" style="left:296px;top:302px;width:258px;">Hot Water System</h2>
  <div class="panel grey" style="left:296px;top:334px;width:258px;height:39px;">
    <ul class="plain-list"><li>Thermaflo 250 Ultre</li></ul>
  </div>

  <h2 class="section-title" style="left:296px;top:382px;width:258px;">Storage Cupboards</h2>
  <div class="panel green" style="left:296px;top:413px;width:258px;height:160px;">
    <dl class="spec">
      <dt>Robes</dt><dd>Aluminium Sliding Mirrored doors with white melamine shelf and hanging rail</dd>
      <dd>2 x open shelf unit to Main Bedroom and 1 x open shelf unit to other bedrooms</dd>
      <dt>Linen/Storage</dt><dd>Aluminium Sliding Vinyl Doors with white melamine four-shelf system</dd>
      <dt>Broom</dt><dd>Single white melamine shelf</dd>
    </dl>
  </div>

  <h2 class="section-title" style="left:296px;top:613px;width:258px;">Electrical</h2>
  <div class="panel grey" style="left:296px;top:644px;width:258px;height:385px;">
    <dl class="spec">
      <dt>Light Points</dt><dd>LED downlights</dd>
      <dt>Powerpoints</dt><dd>Voltline Classic series double power points (white) throughout</dd>
      <dd>Voltline classic series single power pints to Fridge/rangehood/microwave/Garage Door</dd>
      <dt>Smoke Alarms</dt><dd>Hardwired smoke alarms to comply with QLD smoke alarm legislation</dd>
      <dt>TV Point</dt><dd>Tv points located in living rooms/theatres/Master Bedrooms</dd>
      <dt>TV Antennae</dt><dd>Digital compliant tv antennae</dd>
      <dt>NBN</dt><dd>Distribution cabinet all internal data cables to terminate this point</dd>
      <dt>Safety Switches</dt><dd>Safety switches to meter box to comply with current QLD Electrical legislation</dd>
    </dl>
  </div>

  <!-- Right column -->
  <h2 class="section-title" style="left:570px;top:204px;width:259px;">Engineering</h2>
  <div class="panel grey" style="left:570px;top:235px;width:259px;height:218px;">
    <dl class="spec">
      <dt>Wind Rating</dt><dd>C2 Wind Category (AS2870)</dd>
      <dt>Concrete Slab</dt><dd>Engineer designed concrete slab to meet M Class foundation type(AS2870)</dd>
      <dt>Framing</dt><dd>Timber and concrete block framing as per design plans and engineer specifications</dd>
      <dt>Roof Trusses</dt><dd>Designed to Manufacturers specifications</dd>
    </dl>
  </div>

  <h2 class="section-title" style="left:570px;top:465px;width:259px;">Termite Protection</h2>
  <div class="panel grey" style="left:570px;top:496px;width:259px;height:154px;">
    <dl class="spec">
      <dt>Framing</dt><dd>LOSP treated timber framing and roof trusses</dd>
      <dt>Mouldings</dt><dd>LOSP treated architraves/skirtings and door reveals</dd>
      <dt>Slab</dt><dd>Penetration collars</dd>
    </dl>
  </div>

  <h2 class="section-title" style="left:570px;top:664px;width:259px;">Preliminaries</h2>
  <div class="panel green" style="left:570px;top:698px;width:259px;height:174px;">
    <ul class="plain-list">
      <li>Consulting Engineer</li>
      <li>Building Design Plans</li>
      <li>Surveyor Setout of Building</li>
      <li>Construction Works Insurance</li>
      <li>Colour consultancy</li>
      <li>QBRA Home owners warranty insurance</li>
      <li>Building and Plumbing application fees</li>
      <li>6-star minimum energy rating</li>
    </ul>
  </div>

  <div class="contact">
    <p>For more information on our award-winning home designs and the latest information on Land Projects in Mackay and the Whitsundays call us today</p>
    <p>CALL - (07) 4900 2185</p>
    <p class="line">EMAIL - info@harbourhomesnq.com</p>
  </div>

  <div class="photo photo-bath" role="img" aria-label="Bright bathroom with a freestanding bath"></div>
  <div class="grey-veil"></div>
  <div class="photo photo-books" role="img" aria-label="Built-in bookshelves filled with books"></div>
  <div class="grey-veil-mid"></div>
  <div class="photo photo-roof" role="img" aria-label="Terracotta roof tiles"></div>
</div>
</body>
</html>
```